Zelvora - Creative Robotics

We are a software house for Audio Visual Systems integration/automation and home automation. we develop innovative software to automate a variety of devices mainly related to audio visuals and we design touch panel user interfaces to control these systems.

We would like to see designs that stick to our colours and theme, which you can find on our webpage www.zelvora-sample.com.au

The final design should communicate touch panels, innovation, software and automation.

Industry/Entity Type

Software

Requirements
Must have
• The business card must show the following information:
Name example : Derek Halvey
Qualification example: B Eng ICT(CompSys) Dip EngPrac
Title example : Control Systems Programmer
Mobile Phone, Company phone, Email address ,Company website

```html
<!DOCTYPE html>
<html lang="en">
<head>
<meta charset="utf-8">
<title>Zelvora – Business Card</title>
<link rel="stylesheet" href="https://fonts.googleapis.com/css2?family=Montserrat:wght@600;700&family=Questrial&display=swap">
<style>
  :root {
    --backdrop: #8f8f8f;
    --card: #ffffff;
    --brand-blue: #2f8ac9;
    --brand-green: #2e9e5e;
    --symbol-fill: #3aa56c;
    --ink: #4a4a4a;
    --ink-soft: #5c5c5c;
  }
  * { margin: 0; padding: 0; box-sizing: border-box; }
  html, body { width: 1200px; height: 871px; overflow: hidden; }
  body {
    background: var(--backdrop);
    font-family: "Questrial", "Century Gothic", sans-serif;
    position: relative;
  }
  .card {
    position: absolute;
    width: 530px;
    height: 303px;
    background: var(--card);
    box-shadow: 0 10px 24px rgba(0,0,0,0.28);
    overflow: hidden;
  }
  .card--back { left: 50px; top: 284px; }
  .card--front { left: 620px; top: 284px; }

  /* Back */
  .back-symbol-area {
    position: absolute;
    left: 0; top: 22px;
    width: 270px; height: 250px;
    background: var(--symbol-fill);
  }
  .back-brand {
    position: absolute;
    left: 312px; top: 78px;
    text-align: right;
  }
  .brand-name {
    font-family: "Montserrat", sans-serif;
    font-weight: 600;
    color: var(--brand-blue);
    letter-spacing: -0.5px;
    line-height: 1;
  }
  .back-brand .brand-name { font-size: 44px; }
  .brand-tagline {
    color: var(--brand-green);
    font-size: 12px;
    margin-top: 2px;
  }

  /* Front */
  .front-brand {
    position: absolute;
    left: 34px; top: 30px;
    display: flex;
    align-items: center;
    gap: 14px;
  }
  .brand-square {
    width: 48px; height: 48px;
    background: var(--brand-green);
  }
  .front-brand .brand-name { font-size: 46px; }
  .front-brand .brand-tagline { text-align: right; }

  .person {
    position: absolute;
    left: 130px; top: 122px;
  }
  .person-name {
    font-family: "Montserrat", sans-serif;
    font-weight: 700;
    font-size: 19px;
    letter-spacing: 2px;
    color: var(--ink);
  }
  .person-qual {
    font-family: "Questrial", sans-serif;
    font-weight: 400;
    font-size: 13px;
    letter-spacing: 0;
  }
  .person-title {
    font-family: "Montserrat", sans-serif;
    font-weight: 700;
    font-size: 13px;
    letter-spacing: 1.2px;
    color: var(--brand-green);
    margin-top: 4px;
  }
  .contacts {
    position: absolute;
    left: 130px; top: 186px;
    list-style: none;
  }
  .contact {
    display: flex;
    align-items: center;
    gap: 12px;
    font-size: 14px;
    color: var(--ink-soft);
    height: 24px;
  }
  .contact svg { width: 14px; height: 14px; fill: var(--brand-green); }
  .website {
    position: absolute;
    left: 130px; top: 262px;
    font-size: 15px;
    color: var(--brand-blue);
  }
  .website-accent { color: var(--brand-green); }
</style>
</head>
<body>

  <section class="card card--back" aria-label="Business card back">
    <div class="back-symbol-area" role="img" aria-label="Large cropped brand symbol area"></div>
    <div class="back-brand">
      <div class="brand-name">zelvora</div>
      <div class="brand-tagline">Creative Robotics</div>
    </div>
  </section>

  <section class="card card--front" aria-label="Business card front">
    <div class="front-brand">
      <div class="brand-square"></div>
      <div>
        <div class="brand-name">zelvora</div>
        <div class="brand-tagline">Creative Robotics</div>
      </div>
    </div>

    <div class="person">
      <div class="person-name">Derek Halvey, <span class="person-qual">B Eng ICT</span></div>
      <div class="person-title">Control Systems Programmer</div>
    </div>

    <ul class="contacts">
      <li class="contact">
        <svg viewBox="0 0 24 24" aria-hidden="true"><path d="M2 9c0-3 4-5 10-5s10 2 10 5v2h-5V9c-2-1-8-1-10 0v2H2zM6 12h12l3 8H3z"/></svg>
        1.800.555.0147
      </li>
      <li class="contact">
        <svg viewBox="0 0 24 24" aria-hidden="true"><path d="M7 1h10a2 2 0 0 1 2 2v18a2 2 0 0 1-2 2H7a2 2 0 0 1-2-2V3a2 2 0 0 1 2-2zm0 3v14h10V4zm5 15.5a1.2 1.2 0 1 0 0 2.4 1.2 1.2 0 0 0 0-2.4z"/></svg>
        604.555.0182
      </li>
      <li class="contact">
        <svg viewBox="0 0 24 24" aria-hidden="true"><path d="M2 5h20v14H2zm2 2v1l8 5 8-5V7l-8 5z"/></svg>
        dh@halveyhomeworks.ca
      </li>
    </ul>

    <div class="website">www.<span class="website-accent">zelvora-sample</span>.ca</div>
  </section>

</body>
</html>
```